Tax & Accounting business needs business card design

Looking for a professional classy business card for a tax and accounting business. We offer quality, professional services to individuals and small businesses including tax preparation and planning, accounting and bookkeeping, payroll services, and business consulting.

I am an Enrolled Agent (EA) which is a Federally Licensed Tax Practitioner. I am licensed to represent taxpayers before the BTQ.

We want to stand out from all the other "boring" tax & accounting firms without being over the top.

We have a well established firm in one location and are now opening a second location.

Industry/Entity Type

Accounting

Requirements
Must have
• Logo
• Logo color scheme
• Both location addresses
• Front and back of card
• Please see my sample business card (attached) for location addresses, phone numbers, ect. Although you may get some inspiration from this sample card, this is my own unqualified and bad attempt at designing my own card which I'm not happy with.

```html
<!DOCTYPE html>
<html lang="en">
<head>
<meta charset="utf-8">
<title>Ledgerpoint Tax Group – Business Cards</title>
<link href="https://fonts.googleapis.com/css2?family=Tenor+Sans&display=swap" rel="stylesheet">
<style>
  :root {
    --teal: #0f6b68;
    --teal-dark: #0b5553;
    --slate: #4a4a4c;
    --paper: #f7f7f5;
    --ink-light: #ececec;
    --ink-grey: #6b6b6b;
    --backdrop: #2a2a2a;
  }
  * { box-sizing: border-box; margin: 0; padding: 0; }
  html, body { width: 1200px; height: 900px; overflow: hidden; }
  body {
    background: var(--backdrop);
    font-family: "Tenor Sans", "Optima", sans-serif;
    position: relative;
  }
  .card {
    position: absolute;
    left: 280px;
    width: 640px;
    height: 366px;
    background: var(--paper);
    overflow: hidden;
    box-shadow: 0 12px 30px rgba(0,0,0,.45);
  }
  .card--contact { top: 64px; }
  .card--services { top: 470px; }
  .card__art { position: absolute; inset: 0; width: 100%; height: 100%; }

  .brand {
    position: absolute;
    display: flex;
    align-items: center;
    gap: 10px;
    color: var(--teal);
    font-size: 26px;
    line-height: 1.05;
  }
  .brand__dot {
    width: 16px; height: 16px; border-radius: 50%;
    background: currentColor; flex: none;
  }
  .brand__name small { display: block; font-size: 14px; letter-spacing: .12em; }

  /* contact side */
  .card--contact .brand { left: 40px; top: 112px; }
  .holder { position: absolute; right: 36px; top: 40px; text-align: right; }
  .holder__name { color: var(--teal); font-size: 21px; }
  .holder__name span { font-size: 12px; }
  .holder__email { color: var(--ink-grey); font-size: 12px; margin-top: 3px; }
  .office {
    position: absolute;
    text-align: right;
    font-style: normal;
    color: var(--ink-light);
    font-size: 13px;
    line-height: 1.4;
    padding-right: 10px;
    border-right: 1px solid var(--ink-light);
  }
  .office__title { font-size: 14px; }
  .office__lines { margin-top: 12px; }
  .office--santa-fe { right: 290px; top: 212px; }
  .office--albuquerque { right: 30px; top: 150px; }

  /* services side */
  .card--services .brand { color: #fff; left: 50%; transform: translateX(-50%); top: 26px; font-size: 24px; }
  .services {
    position: absolute; left: 0; right: 0; top: 88px;
    text-align: center; color: #fff; font-size: 14px; line-height: 1.3;
  }
  .services__lead { font-size: 15px; }
  .services__license { margin-top: 8px; }
  .services__web { margin-top: 4px; font-size: 18px; letter-spacing: .03em; }
  .credential {
    position: absolute; right: 30px; top: 212px;
    text-align: right; color: var(--teal); font-size: 15px; line-height: 1.35;
  }
</style>
</head>
<body>

<section class="card card--contact" aria-label="Contact side">
  <svg class="card__art" viewBox="0 0 640 366" aria-hidden="true">
    <path d="M0,232 C200,205 420,130 640,95 L640,366 L0,366 Z" fill="var(--slate)"/>
    <path d="M0,218 C160,198 320,162 480,126 C320,175 160,208 0,234 Z" fill="var(--teal)"/>
    <path d="M0,366 L0,318 C60,308 120,295 170,282 C120,315 70,345 40,366 Z" fill="var(--paper)"/>
  </svg>

  <div class="brand">
    <span class="brand__dot"></span>
    <span class="brand__name">Ledgerpoint<small>TAX GROUP LLC</small></span>
  </div>

  <div class="holder">
    <p class="holder__name">Marisol T. Vega, <span>EA</span></p>
    <p class="holder__email">marisol@ledgerpointabq.com</p>
  </div>

  <address class="office office--santa-fe">
    <p class="office__title">Santa Fe Office</p>
    <p>840 Canyon Vista Rd Ste B</p>
    <p>Santa Fe, NM 87505</p>
    <p class="office__lines">office: 505.555.0146<br>fax: 505.555.0147</p>
  </address>

  <address class="office office--albuquerque">
    <p class="office__title">Albuquerque Office</p>
    <p>4410 Mesa Ridge Blvd NE</p>
    <p>Albuquerque, NM 87112</p>
    <p class="office__lines">office: 505.555.0188<br>fax: 505.555.0177</p>
  </address>
</section>

<section class="card card--services" aria-label="Services side">
  <svg class="card__art" viewBox="0 0 640 366" aria-hidden="true">
    <path d="M0,0 H640 V175 C420,195 200,250 0,300 Z" fill="var(--teal)"/>
    <path d="M0,312 C240,296 440,282 640,276" fill="none" stroke="var(--teal)" stroke-width="2"/>
    <path d="M0,322 C240,306 440,292 640,286 C450,304 240,330 0,348 Z" fill="var(--teal-dark)"/>
  </svg>

  <div class="brand">
    <span class="brand__dot"></span>
    <span class="brand__name">Ledgerpoint<small>TAX GROUP LLC</small></span>
  </div>

  <div class="services">
    <p class="services__lead">Professional Business Services</p>
    <p>Taxes - Accounting - Bookkeeping - Payroll</p>
    <p>for individuals and small businesses</p>
    <p class="services__license">Licensed to Represent Taxpayers Before the BTQ</p>
    <p class="services__web">www.ledgerpoint-nm.com</p>
  </div>

  <div class="credential">
    <p>Enrolled Agent</p>
    <p>Federally Licensed Tax Practitioner</p>
  </div>
</section>

</body>
</html>
```